3rd Annual Foam & Fetch Fundraiser

This is our 3rd Annual Foam & Fetch Dog Wash Extravagana to support Allies of Marlowe Valley Pet Center. Please see the attached flyer for the 2nd Annual. We loved this flyer! Please revamp with our logo attached and the new content provided. Let's keep to the same colors as the 2nd Annual flyer-no change. Date: Saturday April 25th 2020 10A-1PM. Rain Date: May 2nd. Same address as 2nd Annual.

Other font styles liked:
• See 2nd Annual Flyer

Colors
add136
e34297
6b449b

Requirements
Must have
• See attached 2nd annual flyer including colors
Nice to have

```html
<!DOCTYPE html>
<html lang="en">
<head>
<meta charset="utf-8">
<title>3rd Annual Foam &amp; Fetch Doggie Wash Extravaganza</title>
<link href="https://fonts.googleapis.com/css2?family=Fredoka:wght@500;600&family=Open+Sans:ital,wght@0,600;0,700;1,600&display=swap" rel="stylesheet">
<style>
  :root {
    --green: #add136;
    --pink: #e34297;
    --purple: #6b449b;
    --ink: #2b2b2b;
    --paper: #ffffff;
    --backdrop: #e6e6e6;
    --social-blue: #3b5998;
  }
  html, body { margin: 0; width: 1200px; height: 1200px; overflow: hidden; background: var(--backdrop); }
  .flyer {
    position: absolute; left: 176px; top: 0;
    width: 924px; height: 1308px;
    transform: scale(0.91743); transform-origin: 0 0;
    background: var(--paper); overflow: hidden;
    font-family: "Open Sans", sans-serif; color: var(--ink);
  }
  .flyer-art { position: absolute; inset: 0; }
  .abs { position: absolute; margin: 0; }
  .display { font-family: "Fredoka", sans-serif; font-weight: 600; line-height: 1; }
  .edition { left: 53px; top: 494px; font-size: 42px; color: var(--pink); }
  .event-name { left: 50px; top: 536px; font-size: 60px; color: var(--purple); letter-spacing: -1px; }
  .event-name .accent { color: var(--green); }
  .tagline { left: 53px; top: 592px; font-size: 15px; font-weight: 700; letter-spacing: 8.6px; color: var(--pink); }
  .subtitle { left: 52px; top: 608px; font-size: 41px; color: var(--green); }
  .pill-text { left: 53px; top: 675px; font-size: 33px; color: var(--paper); }
  .support-label { left: 696px; top: 578px; font-family: "Fredoka", sans-serif; font-weight: 500; font-size: 24px; }
  .partner-mark { left: 688px; top: 628px; width: 200px; display: flex; align-items: center; gap: 10px;
    font-family: "Fredoka", sans-serif; font-weight: 600; font-size: 22px; line-height: 1.15; color: var(--ink); }
  .partner-mark .dot, .sponsor-mark .dot { flex: none; width: 34px; height: 34px; border-radius: 50%; background: var(--ink); }
  .label { font-family: "Fredoka", sans-serif; font-weight: 600; font-size: 34px; color: var(--pink); }
  .value { font-family: "Fredoka", sans-serif; font-weight: 500; font-size: 25px; line-height: 30px; }
  .features { position: absolute; top: 893px; margin: 0; padding: 0; list-style: none; font-weight: 600; font-size: 18px; line-height: 22.5px; }
  .features li { position: relative; padding-left: 25px; }
  .features li svg { position: absolute; left: 0; top: 5px; }
  .donate-line { left: 52px; top: 978px; font-weight: 700; font-size: 18px; }
  .donate-line .url { color: var(--paper); }
  .donate-button { left: 608px; top: 968px; width: 124px; height: 44px; background: var(--paper);
    border: 1px solid var(--social-blue); box-sizing: border-box; display: flex; align-items: center; gap: 6px; padding-left: 4px; }
  .donate-button .square { width: 36px; height: 36px; background: var(--social-blue); }
  .donate-button span { color: var(--social-blue); font-weight: 600; font-size: 17px; line-height: 18px; }
  .note { left: 52px; top: 1016px; font-style: italic; font-weight: 600; font-size: 17.5px; line-height: 23px; }
  .contact { width: 300px; text-align: center; font-size: 17.5px; line-height: 23px; font-weight: 600; white-space: nowrap; }
  .contact .name { font-family: "Fredoka", sans-serif; font-weight: 500; font-size: 26px; line-height: 32px; color: var(--purple); }
  .sponsor-mark { display: flex; justify-content: center; align-items: center; gap: 8px; margin-top: 14px;
    font-family: "Fredoka", sans-serif; font-weight: 600; font-size: 22px; color: var(--ink); }
  .sponsor-mark .dot { width: 26px; height: 26px; }
</style>
</head>
<body>
<main class="flyer">
  <svg class="flyer-art" viewBox="0 0 924 1308" width="924" height="1308">
    <defs>
      <linearGradient id="wash-scene" x1="0" y1="0" x2="1" y2="1">
        <stop offset="0" stop-color="#8fae7a"/><stop offset="0.5" stop-color="#b9b3a8"/><stop offset="1" stop-color="#7e7a73"/>
      </linearGradient>
      <linearGradient id="volunteers" x1="0" y1="0" x2="0" y2="1">
        <stop offset="0" stop-color="#a9c7e6"/><stop offset="0.5" stop-color="#6f9a4f"/><stop offset="1" stop-color="#c9b9a4"/>
      </linearGradient>
      <linearGradient id="dog-warm" x1="0" y1="0" x2="1" y2="1">
        <stop offset="0" stop-color="#8d6b4a"/><stop offset="1" stop-color="#c8a27a"/>
      </linearGradient>
      <linearGradient id="pup-towel" x1="0" y1="0" x2="1" y2="1">
        <stop offset="0" stop-color="#e9ecef"/><stop offset="1" stop-color="#6b6660"/>
      </linearGradient>
      <linearGradient id="kids-mascot" x1="0" y1="0" x2="1" y2="1">
        <stop offset="0" stop-color="#e8e4dc"/><stop offset="1" stop-color="#a0743f"/>
      </linearGradient>
      <linearGradient id="girl-spaniel" x1="0" y1="0" x2="1" y2="1">
        <stop offset="0" stop-color="#8a5e43"/><stop offset="1" stop-color="#d9c3ae"/>
      </linearGradient>
    </defs>

    <rect role="img" aria-label="Photo: volunteers washing a small dog with a hose beside a shampoo sponsor banner" x="0" y="0" width="924" height="540" fill="url(#wash-scene)"/>
    <path role="img" aria-label="Photo: group of teen volunteers posing with a dog mascot costume" d="M0,0 L425,0 Q405,175 255,222 Q125,255 0,212 Z" fill="url(#volunteers)" stroke="var(--pink)" stroke-width="8"/>

    <path d="M0,480 Q250,395 520,398 Q760,402 924,530 L924,1308 L0,1308 Z" fill="var(--paper)"/>
    <path d="M0,480 Q250,395 520,398 Q760,402 924,530" fill="none" stroke="var(--pink)" stroke-width="12"/>

    <rect role="img" aria-label="Illustration: line drawing of a dog with floating bubbles" x="390" y="435" width="125" height="95" rx="18" fill="#f4f9e6"/>

    <circle role="img" aria-label="Photo: German shepherd being rinsed with a hose" cx="628" cy="464" r="108" fill="url(#dog-warm)" stroke="var(--paper)" stroke-width="6"/>
    <circle cx="628" cy="464" r="113" fill="none" stroke="var(--pink)" stroke-width="4"/>
    <circle role="img" aria-label="Photo: puppy wrapped in a white towel" cx="745" cy="330" r="86" fill="url(#pup-towel)" stroke="var(--paper)" stroke-width="6"/>
    <circle cx="745" cy="330" r="91" fill="none" stroke="var(--pink)" stroke-width="4"/>
    <circle role="img" aria-label="Photo: two kids with the dog mascot costume" cx="825" cy="462" r="84" fill="url(#kids-mascot)" stroke="var(--paper)" stroke-width="6"/>
    <circle cx="825" cy="462" r="89" fill="none" stroke="var(--pink)" stroke-width="4"/>

    <path d="M0,667 L620,667 A27,27 0 0 1 620,721 L0,721 Z" fill="var(--purple)"/>

    <rect x="0" y="879" width="924" height="200" fill="var(--green)"/>

    <path role="img" aria-label="Photo: girl cuddling a wet cocker spaniel" d="M924,865 Q700,955 668,1308 L924,1308 Z" fill="url(#girl-spaniel)"/>
    <path d="M924,865 Q700,955 668,1308" fill="none" stroke="var(--pink)" stroke-width="6"/>
  </svg>

  <p class="abs display edition">3rd Annual</p>
  <h1 class="abs display event-name">Foam &amp; <span class="accent">Fetch</span></h1>
  <p class="abs tagline">DO A LITTLE. CHANGE A LOT.</p>
  <h2 class="abs display subtitle">Doggie Wash Extravaganza</h2>
  <p class="abs display pill-text">A Family Fun Event For All Ages</p>

  <p class="abs support-label">In Support Of</p>
  <div class="abs partner-mark"><span class="dot"></span><span>Allies of Marlowe Valley Pet Center</span></div>

  <p class="abs label" style="left:52px;top:737px">Date:</p>
  <p class="abs value" style="left:158px;top:742px">Saturday April 25th 2020<br>Rain Date: May 2nd</p>
  <p class="abs label" style="left:52px;top:810px">Time:</p>
  <p class="abs value" style="left:158px;top:816px">10AM-1PM</p>
  <p class="abs label" style="left:488px;top:737px">Location:</p>
  <p class="abs value" style="left:488px;top:772px">48 Harbor Commons Ave.<br>Marlowe FL 32990<br>Crestview Town Center</p>

  <ul class="features" style="left:55px">
    <li><svg width="16" height="12" viewBox="0 0 16 12"><path d="M1,6 L6,11 L15,1" fill="none" stroke="var(--pink)" stroke-width="3"/></svg>FREE Doggie Wash</li>
    <li><svg width="16" height="12" viewBox="0 0 16 12"><path d="M1,6 L6,11 L15,1" fill="none" stroke="var(--pink)" stroke-width="3"/></svg>Food &amp; Beverages</li>
    <li><svg width="16" height="12" viewBox="0 0 16 12"><path d="M1,6 L6,11 L15,1" fill="none" stroke="var(--pink)" stroke-width="3"/></svg>Vendors (FREE give-a-ways)</li>
  </ul>
  <ul class="features" style="left:352px">
    <li><svg width="16" height="12" viewBox="0 0 16 12"><path d="M1,6 L6,11 L15,1" fill="none" stroke="var(--pink)" stroke-width="3"/></svg>Raffle Drawings</li>
    <li><svg width="16" height="12" viewBox="0 0 16 12"><path d="M1,6 L6,11 L15,1" fill="none" stroke="var(--pink)" stroke-width="3"/></svg>Grand Prize</li>
    <li><svg width="16" height="12" viewBox="0 0 16 12"><path d="M1,6 L6,11 L15,1" fill="none" stroke="var(--pink)" stroke-width="3"/></svg>Donations Welcome</li>
  </ul>
  <ul class="features" style="left:649px">
    <li><svg width="16" height="12" viewBox="0 0 16 12"><path d="M1,6 L6,11 L15,1" fill="none" stroke="var(--pink)" stroke-width="3"/></svg>Adoptions by<br>AMVPC</li>
  </ul>

  <p class="abs donate-line">To Make a Donation: <span class="url">https://www.pawgive.example/amvpc/</span></p>
  <div class="abs donate-button"><div class="square"></div><span>Click<br>Donate</span></div>

  <p class="abs note">All domestic breeds from puppies to seniors invited.<br>Please be sure Furry Fido is tolerant of other dogs, crowds and bathing.</p>

  <div class="abs contact" style="left:60px;top:1096px">
    <div class="name">Dana Whitlow</div>
    Harborline Realty Corp.<br>555.201.4410<br>dana@harborlinerealty.example
    <div class="sponsor-mark"><span class="dot"></span><span>Harborline Realty</span></div>
  </div>
  <div class="abs contact" style="left:374px;top:1096px">
    <div class="name">Megan Corliss</div>
    AMVPC<br>555.318.0927<br>megan-c@mailhub.example
    <div class="sponsor-mark"><span class="dot"></span><span>Allies of Marlowe Valley</span></div>
  </div>
</main>
</body>
</html>
```